Stationary - Business Card/Letterhead and envelope design

Details for my new Stationery Design Project will be added soon. , I have two logos I am trying to decide on. I will upload the eps logos shortly. I have attached a file of what i have so far. I need urgently Business cards, but also will need a letterhead template and envelopes.

PLEASE NOTE THE DEADLINE SAYS 2 DAYS but I need business card design in LESS THAN A DAY.

thanks, Details for my new Stationery Design Project will be added soon. , I have two logos I am trying to decide on. I will upload the eps logos shortly. I have attached a file of what i have so far. I need urgently Business cards, but also will need a letterhead template and envelopes.

thanks
Updates

I have uploaded one of the logos you can work with. hopefully the other one comes soon.

details for the business card.

Marnet Dobson

Managing Director

P&K Ventures Ltd

Bda: 1-441-555-0182

Email: marnet@pkvnbda.example

web: www.pkvnbda.example

Industry/Entity Type

Business

```html
<!DOCTYPE html>
<html lang="en">
<head>
<meta charset="utf-8">
<title>P&amp;K Ventures Ltd — Letterhead</title>
<link rel="stylesheet" href="https://fonts.googleapis.com/css2?family=Montserrat:wght@400;500&display=swap">
<style>
  :root {
    --backdrop: #e9e9ea;
    --paper: #ffffff;
    --teal: #2aa3b3;
    --brown: #8a7461;
    --ink-soft: #7b7b7b;
  }
  * { margin: 0; padding: 0; box-sizing: border-box; }
  html, body {
    width: 1200px;
    height: 900px;
    overflow: hidden;
    background: var(--backdrop);
    font-family: "Montserrat", Arial, sans-serif;
  }
  .letterhead {
    position: absolute;
    left: 310px;
    top: 40px;
    width: 580px;
    height: 820px;
    background: var(--paper);
    box-shadow: 0 2px 10px rgba(0,0,0,0.08);
  }
  .brand-name {
    position: absolute;
    left: 44px;
    top: 52px;
    font-size: 26px;
    font-weight: 500;
    letter-spacing: 0.5px;
    color: var(--teal);
  }
  .footer {
    position: absolute;
    left: 0;
    right: 0;
    bottom: 0;
  }
  .footer-details {
    display: flex;
    justify-content: space-between;
    align-items: flex-end;
    padding: 0 24px 10px 28px;
    font-size: 9.5px;
    line-height: 1.45;
    color: var(--ink-soft);
  }
  .address { padding-left: 4px; }
  .contact {
    display: grid;
    grid-template-columns: auto auto;
    column-gap: 14px;
  }
  .contact-item {
    display: flex;
    align-items: center;
    gap: 5px;
  }
  .contact-item svg { width: 8px; height: 8px; flex: none; }
  .footer-band {
    display: flex;
    height: 12px;
  }
  .band-teal { width: 46%; background: var(--teal); }
  .band-gap { width: 4px; background: var(--paper); }
  .band-brown { flex: 1; background: var(--brown); }
</style>
</head>
<body>
  <main class="letterhead">
    <div class="brand-name">P&amp;K Ventures</div>

    <footer class="footer">
      <div class="footer-details">
        <address class="address" style="font-style: normal;">
          14 Harbour Lane<br>
          Hamilton, Bermuda HM 11
        </address>
        <div class="contact">
          <div class="contact-item">
            <svg viewBox="0 0 10 10"><path d="M2 1 L4 1 L4.6 3 L3.5 4 Q4.5 6 6 6.5 L7 5.4 L9 6 L9 8 Q5 9 2.5 6 Q1 4 2 1 Z" fill="var(--teal)"/></svg>
            <span>1-441-555-0182</span>
          </div>
          <div class="contact-item">
            <svg viewBox="0 0 10 10"><rect x="0.5" y="2" width="9" height="6" fill="var(--teal)"/><path d="M0.5 2 L5 5.5 L9.5 2" stroke="#fff" stroke-width="0.8" fill="none"/></svg>
            <span>marnet@pkvnbda.example</span>
          </div>
          <div class="contact-item">
            <svg viewBox="0 0 10 10"><rect x="2.5" y="0.5" width="5" height="9" rx="1" fill="none" stroke="var(--teal)" stroke-width="1.2"/><circle cx="5" cy="7.8" r="0.6" fill="var(--teal)"/></svg>
            <span>1-441-555-0147</span>
          </div>
          <div class="contact-item">
            <svg viewBox="0 0 10 10"><circle cx="5" cy="5" r="4.5" fill="var(--teal)"/><path d="M0.5 5 H9.5 M5 0.5 Q2.5 5 5 9.5 M5 0.5 Q7.5 5 5 9.5" stroke="#fff" stroke-width="0.6" fill="none"/></svg>
            <span>www.pkvnbda.example</span>
          </div>
        </div>
      </div>
      <div class="footer-band">
        <div class="band-teal"></div>
        <div class="band-gap"></div>
        <div class="band-brown"></div>
      </div>
    </footer>
  </main>
</body>
</html>
```